Flyer for local business that installs fences and sells fence materials

We recently began selling fence materials, in addition to also doing fence installations. We need a flyer that displays our business information and photos of our work, as well as a flyer that shows customers they have the option to buy materials only also.

If they are looking to build a fence - we can help by installing it, or if they want to install themselves, they can buy the materials only from us too. We provide a lifetime warranty on all materials and installations. More information about the company is here: www.BrookvaleRailWorks.com

Its important to have the company logo, phone number, email and business hours listed (Monday - Thursday 9AM - 3PM, Friday 9AM - 1PM).

It is also important to show the fence material types we offer:
Wood, Chainlink, Vinyl and Aluminum
Updates

Updated with more photos and url to website www.brookvalerailworks.com for details

Target Market(s)

Residential Homeowners

Industry/Entity Type

Construction

Font styles to use
Sans Serif
Other font styles liked:
• Arial

Colors
0054AA
0677BA
7BADD7
CADEEF
E8F1F8

Requirements
Must have
• Photos of the fencing we offer
Nice to have
• A way to explain to customers they can hire us to install, or just buy the materials from us
Should not have
• Too many colors or too many words

```html
<!DOCTYPE html>
<html lang="en">
<head>
<meta charset="utf-8">
<title>Brookvale Rail Works Flyer</title>
<link href="https://fonts.googleapis.com/css2?family=Oswald:wght@600&family=Poppins:wght@400;500;600;700;800&display=swap" rel="stylesheet">
<style>
:root{
  --blue:#3d86cc;
  --orange:#f7931e;
  --gold:#e8a04a;
  --brown:#55392a;
  --ink:#1d1d1d;
  --paper:#ffffff;
  --backdrop:#cbcbcb;
  --rule:#d9d9d9;
}
*{margin:0;padding:0;box-sizing:border-box}
html,body{width:1200px;height:2378px;overflow:hidden;background:var(--backdrop);font-family:'Poppins',Arial,sans-serif}
.flyer{position:absolute;left:94px;top:534px;width:1012px;height:1310px;background:var(--paper);overflow:hidden;box-shadow:0 10px 30px rgba(0,0,0,.25)}
.abs{position:absolute}
.hero-art{left:0;top:0}
.brand{left:68px;top:78px;display:flex;align-items:flex-start;gap:18px}
.brand-mark{width:86px;height:110px;background:var(--brown)}
.brand-name{font-weight:800;font-size:34px;color:var(--blue);line-height:1.1;margin-top:6px}
.brand-phone{font-weight:800;font-size:34px;color:var(--ink);line-height:1.15}
.brand-tag{font-weight:700;font-size:12.5px;color:var(--ink);margin-top:4px}
.headline{left:70px;top:226px;font-family:'Oswald',Arial,sans-serif;font-weight:600;font-size:72px;line-height:1;color:var(--gold);letter-spacing:-1px;white-space:nowrap;transform:scaleX(.88);transform-origin:left top}
.subhead{left:76px;top:312px;font-weight:800;font-size:33px;line-height:1.05;color:var(--brown)}
.mission{left:68px;top:412px;width:520px;color:#fff}
.mission h2{font-size:24px;font-weight:700;line-height:1.1;margin-bottom:6px}
.mission p{font-size:15.5px;line-height:1.15}
.features{left:68px;top:538px;width:425px;list-style:none}
.features li{display:flex;align-items:flex-start;gap:12px;font-size:20px;line-height:1.25;font-weight:500;color:var(--ink);padding:6px 0 7px;border-bottom:1px solid var(--rule)}
.features li:last-child{border-bottom:none}
.features svg{flex:none;margin-top:5px}
.features small{display:block;font-size:20px;font-weight:400;line-height:1.2}
.styles{left:544px;top:542px;display:grid;grid-template-columns:195px 195px;gap:13px 10px}
.style-card{display:flex;flex-direction:column;height:161px}
.style-card .photo{flex:1}
.style-card span{background:var(--orange);color:#fff;font-size:14px;font-weight:500;text-align:center;height:25px;line-height:25px}
.ph-wood{background:linear-gradient(135deg,#c89a63,#e3c291 60%,#8b6a44)}
.ph-chain{background:linear-gradient(180deg,#b9c6cc,#7d8a66 55%,#5b6a3c)}
.ph-vinyl{background:linear-gradient(180deg,#3e6aa8 0%,#8fa6c0 35%,#eeeeee 60%,#cfcfcf)}
.ph-alu{background:linear-gradient(180deg,#e9eef2,#b9c2c9 60%,#8b949b)}
.tagband{left:0;top:895px;width:1012px;height:100px;background:var(--blue);color:#fff;font-weight:600;font-size:26px;line-height:1.2;padding:17px 0 0 70px}
.estimate{left:69px;top:1013px;width:380px}
.estimate .lead{display:flex;align-items:center;gap:12px}
.estimate .lead b{font-size:27px;font-weight:800;line-height:1.02;color:var(--ink)}
.estimate .free{font-size:64px;font-weight:800;color:var(--orange);line-height:1}
.estimate p{font-size:18px;line-height:1.15;color:var(--ink);margin-top:2px}
.hours{left:468px;top:1012px;width:473px;height:110px;display:grid;grid-template-columns:285px 188px;border-radius:6px;overflow:hidden;font-weight:700;font-size:28px;color:#fff}
.hours .day{background:var(--brown);padding-left:15px;border-right:3px solid #fff}
.hours .time{background:var(--orange);padding-left:13px}
.hours div{display:flex;align-items:center;height:55px}
.hours .top{border-bottom:2px dashed rgba(255,255,255,.6)}
.footer-art{left:0;top:1157px}
.contact{left:68px;top:1184px;color:#fff;font-weight:800;font-size:28px;line-height:1.05}
.cta{left:290px;top:1176px;color:#fff;font-weight:600;font-size:18px}
.details{left:288px;top:1219px;display:flex;gap:16px;color:#fff;font-size:15px;font-weight:500}
.details span{display:flex;align-items:center;gap:6px}
</style>
</head>
<body>
<main class="flyer">
  <svg class="abs hero-art" width="1012" height="515" viewBox="0 0 1012 515">
    <defs>
      <linearGradient id="yard" x1="0" y1="0" x2="0" y2="1">
        <stop offset="0" stop-color="#3f4f2c"/>
        <stop offset=".35" stop-color="#6f7d4a"/>
        <stop offset=".55" stop-color="#d8c08f"/>
        <stop offset="1" stop-color="#7a6b3f"/>
      </linearGradient>
    </defs>
    <polygon points="660,0 1012,0 1012,515 680,515 530,260" fill="#e8a04a"/>
    <polygon points="680,0 1012,0 1012,515 690,515 547,260" fill="url(#yard)" role="img" aria-label="Photo of an installer building a wooden privacy fence in a grassy yard"/>
    <polygon points="0,400 615,400 685,515 0,515" fill="#3d86cc"/>
  </svg>

  <div class="abs brand">
    <div class="brand-mark"></div>
    <div>
      <div class="brand-name">Brookvale Rail Works</div>
      <div class="brand-phone">555-014-2270</div>
      <div class="brand-tag">“Because Good Fences Make Good Neighbors”</div>
    </div>
  </div>

  <h1 class="abs headline">WE BUILD FENCES</h1>
  <div class="abs subhead">AND WE WOULD LOVE TO<br>BUILD YOUR FENCE TOO!</div>

  <section class="abs mission">
    <h2>OUR MISSION</h2>
    <p>We strive to provide our customers with the best fence experience possible. We want your fence installation process to go smoothly and easily, from start to finish</p>
  </section>

  <ul class="abs features">
    <li><svg width="16" height="16" viewBox="0 0 16 16"><circle cx="8" cy="8" r="8" fill="#f7931e"/><path d="M4.5 8.2l2.3 2.3 4.7-4.8" stroke="#fff" stroke-width="2" fill="none"/></svg>Free Estimates</li>
    <li><svg width="16" height="16" viewBox="0 0 16 16"><circle cx="8" cy="8" r="8" fill="#f7931e"/><path d="M4.5 8.2l2.3 2.3 4.7-4.8" stroke="#fff" stroke-width="2" fill="none"/></svg>Professional Installation</li>
    <li><svg width="16" height="16" viewBox="0 0 16 16"><circle cx="8" cy="8" r="8" fill="#f7931e"/><path d="M4.5 8.2l2.3 2.3 4.7-4.8" stroke="#fff" stroke-width="2" fill="none"/></svg>Concrete in EVERY Post</li>
    <li><svg width="16" height="16" viewBox="0 0 16 16"><circle cx="8" cy="8" r="8" fill="#f7931e"/><path d="M4.5 8.2l2.3 2.3 4.7-4.8" stroke="#fff" stroke-width="2" fill="none"/></svg>HOA Submission Assistance</li>
    <li><svg width="16" height="16" viewBox="0 0 16 16"><circle cx="8" cy="8" r="8" fill="#f7931e"/><path d="M4.5 8.2l2.3 2.3 4.7-4.8" stroke="#fff" stroke-width="2" fill="none"/></svg>Lifetime Workmanship Warranty</li>
    <li><svg width="16" height="16" viewBox="0 0 16 16"><circle cx="8" cy="8" r="8" fill="#f7931e"/><path d="M4.5 8.2l2.3 2.3 4.7-4.8" stroke="#fff" stroke-width="2" fill="none"/></svg>Experienced Installation Teams</li>
    <li><svg width="16" height="16" viewBox="0 0 16 16"><circle cx="8" cy="8" r="8" fill="#f7931e"/><path d="M4.5 8.2l2.3 2.3 4.7-4.8" stroke="#fff" stroke-width="2" fill="none"/></svg>Quality Workmanship &amp; Materials</li>
    <li><svg width="16" height="16" viewBox="0 0 16 16"><circle cx="8" cy="8" r="8" fill="#f7931e"/><path d="M4.5 8.2l2.3 2.3 4.7-4.8" stroke="#fff" stroke-width="2" fill="none"/></svg><div>FREE Gate Adjustments for LIFE<small>some restrictions apply</small></div></li>
  </ul>

  <div class="abs styles">
    <figure class="style-card"><div class="photo ph-wood" role="img" aria-label="Photo of a wooden privacy fence"></div><span>Wood Fences</span></figure>
    <figure class="style-card"><div class="photo ph-chain" role="img" aria-label="Photo of a chainlink fence on a grassy slope"></div><span>Chainlink Fences</span></figure>
    <figure class="style-card"><div class="photo ph-vinyl" role="img" aria-label="Photo of a white vinyl fence by houses"></div><span>Vinyl Fences</span></figure>
    <figure class="style-card"><div class="photo ph-alu" role="img" aria-label="Photo of wrapped aluminum fence panels"></div><span>Aluminum Fences</span></figure>
  </div>

  <div class="abs tagband">Beautiful, professionally installed fences at affordable prices!<br>Many fence styles available.</div>

  <section class="abs estimate">
    <div class="lead"><b>ESTIMATES<br>ARE ALWAYS</b><span class="free">FREE</span></div>
    <p>If you know your measurements OR have a lot survey, email or call us for a virtual estimate!</p>
  </section>

  <div class="abs hours">
    <div class="day top">MONDAY - THURS</div>
    <div class="time top">9AM - 3PM</div>
    <div class="day">FRIDAY</div>
    <div class="time">9AM - 1PM</div>
  </div>

  <svg class="abs footer-art" width="1012" height="153" viewBox="0 0 1012 153">
    <rect x="230" y="10" width="782" height="45" fill="#f7931e"/>
    <rect x="230" y="55" width="782" height="98" fill="#55392a"/>
    <polygon points="0,0 230,0 270,75 220,153 0,153" fill="#3d86cc"/>
    <polyline points="236,0 276,75 226,153" fill="none" stroke="#fff" stroke-width="6"/>
  </svg>
  <div class="abs contact">CONTACT<br>US TODAY</div>
  <div class="abs cta">Call, email, or message us online to schedule an in-person estimate</div>
  <div class="abs details">
    <span><svg width="15" height="15" viewBox="0 0 24 24"><path d="M6.6 10.8a15 15 0 006.6 6.6l2.2-2.2c.3-.3.7-.4 1-.2 1.1.4 2.3.6 3.6.6.6 0 1 .4 1 1V20c0 .6-.4 1-1 1A17 17 0 013 4c0-.6.4-1 1-1h3.5c.6 0 1 .4 1 1 0 1.3.2 2.5.6 3.6.1.3 0 .7-.2 1z" fill="#f7931e"/></svg>555-014-2270</span>
    <span><svg width="15" height="15" viewBox="0 0 24 24"><circle cx="12" cy="12" r="10" fill="none" stroke="#f7931e" stroke-width="2"/><path d="M2 12h20M12 2c3 3 3 17 0 20M12 2c-3 3-3 17 0 20" fill="none" stroke="#f7931e" stroke-width="2"/></svg>www.brookvalerailworks.com</span>
    <span><svg width="14" height="16" viewBox="0 0 24 28"><path d="M12 1a9 9 0 00-9 9c0 7 9 16 9 16s9-9 9-16a9 9 0 00-9-9z" fill="none" stroke="#f7931e" stroke-width="2.5"/><circle cx="12" cy="10" r="3" fill="#f7931e"/></svg>48 Millbrook Ln, Brookvale NC 28000</span>
  </div>
</main>
</body>
</html>
```